Business Card Design Project

My company is called Carvel Solutions and i sell Spine implants for a company allied Brennad and another called Lumtrail

Contact Information for Business Card

I would like something that incorporates the use of a picture of a spine as i specialize in selling spinal implants

```html
<!DOCTYPE html>
<html lang="en">
<head>
<meta charset="utf-8">
<title>Carvel Solutions – Business Card</title>
<link rel="stylesheet" href="https://fonts.googleapis.com/css2?family=Open+Sans:wght@400;600;700&display=swap">
<style>
  :root {
    --teal: #21a89e;
    --teal-dark: #0f968c;
    --teal-light: #32b3ac;
    --paper: #efede9;
    --ink-grey: #9a9a9a;
    --ink-dark: #6f6f6f;
    --backdrop: #e9e9e7;
    --cream: #f1eee8;
  }
  * { margin: 0; padding: 0; box-sizing: border-box; }
  html, body {
    width: 1200px; height: 800px; overflow: hidden;
    background: var(--backdrop);
    font-family: "Open Sans", Arial, sans-serif;
  }
  .stage { position: relative; width: 1200px; height: 800px; }

  .card {
    position: absolute;
    width: 500px; height: 286px;
    box-shadow: 0 6px 18px rgba(0,0,0,0.12);
  }

  /* Front */
  .card-front {
    left: 70px; top: 160px;
    background: linear-gradient(135deg, var(--teal-light), var(--teal-dark));
    display: flex; align-items: center; justify-content: center; gap: 16px;
  }
  .front-dot {
    width: 34px; height: 34px; border-radius: 50%;
    border: 4px solid var(--cream);
  }
  .front-name {
    color: var(--cream);
    font-weight: 700; font-size: 24px;
    letter-spacing: 1px; text-transform: uppercase;
  }

  /* Back */
  .card-back {
    left: 630px; top: 350px;
    background: var(--paper);
    border-bottom: 4px solid var(--teal);
  }
  .person-name {
    position: absolute; right: 40px; top: 34px;
    color: var(--teal); font-weight: 700; font-size: 19px;
  }
  .brand {
    position: absolute; left: 40px; top: 108px;
    display: flex; align-items: center; gap: 12px;
  }
  .brand-dot {
    width: 30px; height: 30px; border-radius: 50%;
    background: var(--teal);
  }
  .brand-name {
    color: var(--ink-grey); font-weight: 700; font-size: 17px;
    letter-spacing: 0.5px; text-transform: uppercase;
  }
  .contact {
    position: absolute; left: 40px; bottom: 26px;
    list-style: none; font-size: 12.5px; color: var(--ink-dark);
  }
  .contact li { display: flex; align-items: center; gap: 9px; line-height: 20px; }
  .contact svg { width: 12px; height: 12px; fill: var(--teal); flex: none; }
  .website {
    position: absolute; right: 40px; bottom: 30px;
    font-size: 12.5px; color: var(--ink-dark);
  }
  .website strong { color: var(--teal); font-weight: 700; }
</style>
</head>
<body>
<main class="stage">
  <section class="card card-front" aria-label="Card front">
    <span class="front-dot"></span>
    <span class="front-name">Carvel Solutions</span>
  </section>

  <section class="card card-back" aria-label="Card back">
    <h1 class="person-name">Tomas Reyle</h1>
    <div class="brand">
      <span class="brand-dot"></span>
      <span class="brand-name">Carvel Solutions</span>
    </div>
    <ul class="contact">
      <li>
        <svg viewBox="0 0 24 24" aria-hidden="true"><path d="M6.6 10.8a15 15 0 0 0 6.6 6.6l2.2-2.2a1 1 0 0 1 1-.25 11.4 11.4 0 0 0 3.6.57 1 1 0 0 1 1 1V20a1 1 0 0 1-1 1A17 17 0 0 1 3 4a1 1 0 0 1 1-1h3.5a1 1 0 0 1 1 1c0 1.25.2 2.45.57 3.57a1 1 0 0 1-.25 1z"/></svg>
        555 014 2230
      </li>
      <li>
        <svg viewBox="0 0 24 24" aria-hidden="true"><path d="M2 5h20v14H2z M3 6l9 7 9-7" fill="none" stroke="#21a89e" stroke-width="2.4"/></svg>
        tomas@carvelsolutions.com
      </li>
    </ul>
    <p class="website">www.<strong>carvelsolutions</strong>.com</p>
  </section>
</main>
</body>
</html>
```